IT Company needs stationary design

Business cards, MS Word, PowerPoint, A4 notepad design base on our company logo. This must be a set of templates in the same style which could be used both for printable documents as well as for documents shared digitally via email, website etc. This should be a modern design which is still professional, so make sure content is well readable both in MS Word and MS PowerPoint templates.

Target Market(s)

SME and Corporate

Industry/Entity Type

It Company

Font styles to use
Sans Serif

Colors
0455a3
0692cd
f37122
ffc214

Requirements
Must have
• 1) Business cards design: modern but still professional
• 2) MS Word: mostly for IT project documents (business analysis, reports, specifications, etc.) must be professional and easy readable.
• 3) MS PowerPoint: first slide, normal slide, last slide.
• 4) A4 notepad: header (must), footer (must), some light design on the background (optionally)
Nice to have
• Business cards design: would be nice to have 2-4 color variations of the same design from one side - cover (for example part of the cards are blue, part of the cards are orange) and other side with contact details is identical.

```html
<!DOCTYPE html>
<html lang="en">
<head>
<meta charset="utf-8">
<title>Corvanta Business Card</title>
<link href="https://fonts.googleapis.com/css2?family=Roboto:wght@400;500;700&display=swap" rel="stylesheet">
<style>
  :root {
    --navy: #0455a3;
    --blue: #0692cd;
    --orange: #f37122;
    --yellow: #ffc214;
    --ink: #2b2b2d;
    --text: #555759;
    --paper: #f7f7f7;
    --dark-card: #1c1d1f;
    --stage: #e9e9ea;
    --faint-ring: #e4e4e4;
  }
  * { margin: 0; padding: 0; box-sizing: border-box; }
  html, body { width: 1200px; height: 960px; overflow: hidden; }
  body {
    background: var(--stage);
    font-family: "Roboto", Arial, sans-serif;
    position: relative;
  }
  .card {
    position: absolute;
    width: 600px;
    height: 342px;
    border-radius: 18px;
    overflow: hidden;
  }
  .card-front {
    left: 315px; top: 113px;
    background: var(--paper);
  }
  .card-back {
    left: 311px; top: 473px;
    background: var(--dark-card);
  }
  .faint-ring {
    position: absolute;
    left: 303px; top: 90px;
    width: 298px; height: 298px;
    border: 16px solid var(--faint-ring);
    border-radius: 50%;
  }
  .notch {
    position: absolute;
    right: -16px; top: 36px;
    width: 32px; height: 36px;
    border-radius: 50%;
    background: var(--dark-card);
  }
  .wordmark {
    position: absolute;
    display: flex;
    align-items: center;
  }
  .wordmark-dot {
    border-radius: 50%;
    border-style: solid;
  }
  .wordmark-name { font-weight: 400; }
  .card-front .wordmark { left: 37px; top: 40px; gap: 16px; }
  .card-front .wordmark-dot { width: 78px; height: 78px; border-width: 5px; border-color: var(--ink); }
  .card-front .wordmark-name { font-size: 36px; color: var(--ink); }

  .holder {
    position: absolute;
    right: 41px; top: 33px;
    text-align: right;
  }
  .holder-name { font-size: 21px; font-weight: 700; color: var(--blue); line-height: 24px; }
  .holder-role { font-size: 15px; font-weight: 500; color: var(--orange); line-height: 20px; }

  .address {
    position: absolute;
    left: 37px; top: 164px;
    font-size: 14.5px;
    line-height: 18px;
    color: var(--text);
  }
  .contact-list {
    position: absolute;
    left: 37px; top: 208px;
    list-style: none;
  }
  .contact-list li {
    display: flex;
    align-items: center;
    gap: 8px;
    height: 19px;
    font-size: 14.5px;
    color: var(--text);
  }
  .contact-list svg { width: 14px; height: 14px; fill: var(--blue); }

  .card-back .wordmark {
    left: 0; right: 0; top: 70px;
    flex-direction: column;
    gap: 18px;
  }
  .card-back .wordmark-dot { width: 130px; height: 130px; border-width: 9px; border-color: #ffffff; }
  .card-back .wordmark-name { font-size: 34px; color: #ffffff; }
  .back-url {
    position: absolute;
    left: 0; right: 0; top: 284px;
    text-align: center;
    color: #ffffff;
    font-size: 15px;
    letter-spacing: 7px;
  }
</style>
</head>
<body>
  <section class="card card-front">
    <div class="faint-ring" aria-hidden="true"></div>
    <div class="notch" aria-hidden="true"></div>
    <div class="wordmark">
      <span class="wordmark-dot" aria-hidden="true"></span>
      <span class="wordmark-name">corvanta</span>
    </div>
    <div class="holder">
      <p class="holder-name">DANIEL REYES</p>
      <p class="holder-role">CEO/FOUNDER</p>
    </div>
    <p class="address">4120 Willow Court<br>Fairbanks, Alaska 34210</p>
    <ul class="contact-list">
      <li><svg viewBox="0 0 16 16" aria-hidden="true"><path d="M3.5 1l2.6 3-1.4 1.8c.9 2 2.6 3.7 4.6 4.6L11 9l3 2.6-1.4 2.8C7 14 2 9 1.6 3.4z"/></svg>612 470 3851</li>
      <li><svg viewBox="0 0 16 16" aria-hidden="true"><path d="M4.5 0h7a1 1 0 0 1 1 1v14a1 1 0 0 1-1 1h-7a1 1 0 0 1-1-1V1a1 1 0 0 1 1-1zm.8 2v10h5.4V2zM8 12.8a.9.9 0 1 0 0 1.8.9.9 0 0 0 0-1.8z"/></svg>845 219 6073</li>
      <li><svg viewBox="0 0 16 16" aria-hidden="true"><path d="M4 1h8v4H4zM1 6h14v7h-3v2H4v-2H1zm4 5v3h6v-3z"/></svg>493 508 2716</li>
      <li><svg viewBox="0 0 16 16" aria-hidden="true"><path d="M1 3h14v10H1zm1.5 1.3V5l5.5 4 5.5-4v-.7z"/></svg>daniel@corvanta.com</li>
      <li><svg viewBox="0 0 16 16" aria-hidden="true"><path d="M8 1a7 7 0 1 0 0 14A7 7 0 0 0 8 1zm-1 2.5c-.5 1-1.8 1.2-2.2 2.3.8.6 1.8.3 2.4 1.2.4.8-.4 1.6.2 2.4.6.6 1.3 1.5 1 2.6-1.6-.2-2.4-1.8-3.4-2.8-.8-.9-1.5-2-1.6-3.2C3.8 4.4 5.3 3.4 7 3.5zm3.2.5c1 .6 1.8 1.6 2.1 2.8-.8.3-1.6-.3-2.3-.6-.3-.8.6-1.4.2-2.2z"/></svg>www.corvanta.com</li>
    </ul>
  </section>

  <section class="card card-back">
    <div class="wordmark">
      <span class="wordmark-dot" aria-hidden="true"></span>
      <span class="wordmark-name">corvanta</span>
    </div>
    <p class="back-url">www.corvanta.com</p>
  </section>
</body>
</html>
```